Garden Design Business Card Design

A business card design for garden design company called ;
ROOTED IN CLAY which has a great deal of maintenance but
wishes to promote its expertise for design in planting and garden
design, but in an informal manner.

Would love to see quite a rustic approach,very strong and innovative and taking risks on typography. Am open to ideas with
colours,as memorability is important.

Target Market(s)

General public 40/50 years in a very trendy area

Industry/Entity Type

Business

Contact Information for Business Card

ROOTED IN CLAY. Garden design and maintenance.
Peter Holcombe
Telephone 01632 960417 Mobile 07700 900382

```html
<!DOCTYPE html>
<html lang="en">
<head>
<meta charset="utf-8">
<title>Rooted in Clay – Business Card</title>
<link rel="stylesheet" href="https://fonts.googleapis.com/css2?family=Jura:wght@500;700&display=swap">
<style>
  :root {
    --bg: #b9bbbc;
    --card: #fbfbfb;
    --card-shade: #eceeed;
    --brown: #8a4a1f;
    --ink: #2b2b2b;
    --muted: #6d6d6d;
    --green-light: #8cc94c;
    --green-dark: #4c9630;
  }
  * { margin: 0; padding: 0; box-sizing: border-box; }
  html, body { width: 1200px; height: 894px; overflow: hidden; }
  body {
    background: var(--bg);
    font-family: "Jura", sans-serif;
    position: relative;
  }
  .card {
    position: absolute;
    width: 540px;
    height: 310px;
    background: linear-gradient(135deg, var(--card) 40%, var(--card-shade));
    box-shadow: 0 6px 18px rgba(0,0,0,0.18);
    overflow: hidden;
  }
  .card--front { left: 630px; top: 120px; }
  .card--back { left: 30px; top: 464px; }

  .pill {
    position: absolute;
    right: 0;
    border-radius: 999px 0 0 999px;
    background: radial-gradient(ellipse at 45% 50%, var(--green-light), var(--green-dark));
  }
  .card--front .pill { left: 300px; top: 170px; height: 58px; }
  .card--back .pill { left: 350px; top: 108px; height: 58px; }

  .brand {
    position: absolute;
    display: flex;
    align-items: center;
    gap: 10px;
    color: var(--green-dark);
    font-weight: 700;
    letter-spacing: 1px;
    white-space: nowrap;
  }
  .brand__dot {
    border-radius: 50%;
    background: var(--green-dark);
    flex: none;
  }
  .card--front .brand { left: 50px; top: 80px; font-size: 20px; }
  .card--front .brand__dot { width: 22px; height: 22px; }
  .card--back .brand { left: 368px; top: 226px; font-size: 13px; gap: 8px; }
  .card--back .brand__dot { width: 18px; height: 18px; }

  .contact { position: absolute; left: 30px; top: 32px; width: 320px; }
  .contact__name { color: var(--brown); font-size: 22px; font-weight: 700; }
  .contact__title { color: var(--muted); font-size: 8px; letter-spacing: 1px; margin-top: 2px; }
  .contact__list { margin-top: 14px; display: grid; grid-template-columns: 78px 1fr; row-gap: 4px; font-size: 13px; font-weight: 700; }
  .contact__label { color: var(--brown); }
  .contact__value { color: var(--ink); }

  .rule { position: absolute; left: 30px; height: 1.5px; background: var(--brown); }
  .rule--a { top: 180px; width: 300px; }
  .rule--b { top: 226px; width: 320px; }
  .rule--c { top: 262px; width: 320px; }
  .rule--d { top: 278px; width: 320px; }

  .address {
    position: absolute; left: 30px; top: 194px;
    display: flex; align-items: center; gap: 8px;
    font-size: 12px; font-weight: 700; color: var(--ink);
    white-space: nowrap;
  }
</style>
</head>
<body>
  <section class="card card--front" aria-label="Card front">
    <div class="brand"><span class="brand__dot"></span>ROOTED IN CLAY</div>
    <div class="pill"></div>
  </section>

  <section class="card card--back" aria-label="Card back">
    <div class="contact">
      <div class="contact__name">Peter Holcombe</div>
      <div class="contact__title">GENERAL MANAGER</div>
      <div class="contact__list">
        <span class="contact__label">Phone:</span><span class="contact__value">01632 960417</span>
        <span class="contact__label">Mobile:</span><span class="contact__value">07700 900382</span>
        <span class="contact__label">Email:</span><span class="contact__value">peter@rootedinclay.co.uk</span>
        <span class="contact__label">website:</span><span class="contact__value">www.rootedinclay.co.uk</span>
      </div>
    </div>
    <div class="rule rule--a"></div>
    <div class="address">
      <svg width="12" height="16" viewBox="0 0 12 16" aria-hidden="true">
        <path d="M6 0a6 6 0 0 0-6 6c0 4.5 6 10 6 10s6-5.5 6-10a6 6 0 0 0-6-6z" fill="#8a4a1f"/>
        <circle cx="6" cy="6" r="2.2" fill="#fbfbfb"/>
      </svg>
      14 Orchard Lane, Kilnbrook Green
    </div>
    <div class="rule rule--b"></div>
    <div class="rule rule--c"></div>
    <div class="rule rule--d"></div>
    <div class="pill"></div>
    <div class="brand"><span class="brand__dot"></span>ROOTED IN CLAY</div>
  </section>
</body>
</html>
```